Ad-Services Website

The project is for an agency which provides a 360 service around the world of printing and advertising. Without much focus on the advertising per say, but much more focus on the medium on which advertisement can be achieved, such as banners, moving banners, boards and so on.

Futhermore more the company deals with material printing so it has advertising agencies as clients.

Finally it represents several companies in Greece for materials around advertising such as stands, ad-walls, banners and so on.

The webpage needs to have web 2.0 look an feel, and it will lack in content, therefore the focus should not be in large sections of text.

I can have a pdf sent with a small presentation that was done to the client, and the structure to which he agreed to

The following website has the look & feel of what we are looking for

http://www.kolvara.gr

The companies current website where you can get the colors and logos from is

http://trumexsign.gr
Updates

Hello,

Thank you all very much for your designs, we really appreciate your contribution.

Maybe in our next project we can work together.

Best Regards,
Marek

Industry/Entity Type

Advertising

```html
<!DOCTYPE html>
<html lang="en">
<head>
<meta charset="utf-8">
<title>Trumex Advertising</title>
<link rel="stylesheet" href="https://fonts.googleapis.com/css2?family=Source+Sans+3:wght@400;600;700&display=swap">
<style>
:root{
  --teal:#1f6e8c;
  --teal-dark:#2c7390;
  --teal-light:#5aa8c4;
  --ink:#222;
  --text:#666;
  --line:#d9d9d9;
  --footer-bg:#f7f7f7;
  --green:#8cc21c;
}
*{margin:0;padding:0;box-sizing:border-box}
html,body{width:1100px;height:1200px;overflow:hidden;background:#fff}
body{font-family:"Source Sans 3",sans-serif;color:var(--ink);position:relative}
.abs{position:absolute}
/* header */
.brand{left:50px;top:30px;color:#111;line-height:1}
.brand-main{font-size:54px;font-weight:400;letter-spacing:-2px}
.brand-sub{display:block;font-size:27px;color:var(--teal);margin:-8px 0 0 68px;letter-spacing:-0.5px}
.main-nav{right:66px;top:78px;display:flex;align-items:center;font-size:18px;color:var(--teal)}
.main-nav span.sep{display:inline-block;width:1px;height:26px;background:#9ab;transform:rotate(20deg);margin:0 23px}
.header-rule{left:0;top:126px;width:1100px;height:2px;background:#8fb0bd}
/* hero */
.hero{left:0;top:128px;width:1100px;height:406px;background:linear-gradient(180deg,var(--teal-dark),var(--teal-light))}
.slider{left:33px;top:146px;width:663px;height:350px;background:#fff;box-shadow:0 14px 20px rgba(0,0,0,.18)}
.slide-art{left:10px;top:6px;width:651px;height:288px;background:linear-gradient(160deg,#9fd12b,var(--green) 60%,#7cb014)}
.slide-bar{left:10px;top:294px;width:652px;height:48px;background:#dcdcdc}
.dots{left:294px;top:325px;display:flex;gap:4px}
.dots i{width:8px;height:8px;border-radius:50%;background:#999}
.dots i:first-child{background:#111}
.apps{left:707px;top:146px;width:348px;height:350px;background:#fff;box-shadow:0 14px 20px rgba(0,0,0,.18)}
.apps-card{left:10px;top:7px;width:331px;height:333px;border:1px solid #eee;border-radius:4px}
.apps-title{left:28px;top:18px;font-size:22px;color:var(--teal)}
.app{left:25px;display:flex;gap:10px}
.app-thumb{width:98px;height:74px;border:2px solid #e4e4e4;box-shadow:0 1px 3px rgba(0,0,0,.2);background:linear-gradient(135deg,#5b8fc0,#c9a56e)}
.app h3{font-size:13px;font-weight:400;color:#222;margin:1px 0 6px}
.app p{font-size:10.5px;line-height:19px;color:#333;width:175px}
/* welcome */
.welcome{left:47px;top:569px;width:985px}
.welcome h1{font-size:20px;font-weight:400;color:#222;margin-bottom:10px}
.welcome .lead{font-size:12.5px;font-weight:700;color:#333;line-height:20px;text-align:justify;margin-bottom:6px}
.welcome p{font-size:12.3px;color:var(--text);line-height:20px;text-align:justify;margin-bottom:6px}
.divider{left:33px;top:811px;width:1024px;height:1px;background:var(--line)}
/* partners */
.partner-mark{left:67px;top:830px}
.partners{left:250px;top:850px;width:760px;display:flex;justify-content:space-between;font-size:20px;font-weight:700;color:var(--teal)}
/* footer */
.footer{left:0;top:911px;width:1100px;height:226px;background:var(--footer-bg);border-top:2px solid #eee}
.fcol{top:36px}
.fcol h4{font-size:15.5px;font-weight:400;color:var(--teal);margin-bottom:12px}
.fcol li{list-style:none;font-size:12.5px;color:var(--teal);line-height:25.5px}
.fsep{top:56px;width:1px;height:128px;background:#e2e2e2}
.contact strong{font-weight:600}
.contact .tel{font-size:16px}
.contact u{text-decoration:underline}
.bottom{left:0;top:1136px;width:1100px;height:64px;border-top:1px solid #ddd;background:#fff}
.copy{left:58px;top:15px;font-size:11px;color:#555}
.social{right:60px;top:14px;display:flex;gap:6px}
.social i{width:22px;height:22px;border-radius:50%;background:#555}
</style>
</head>
<body>
<header>
  <div class="abs brand"><span class="brand-main">trumex</span><span class="brand-sub">advertising</span></div>
  <nav class="abs main-nav">About Us<span class="sep"></span>Advertising<span class="sep"></span>Displays<span class="sep"></span>Printing<span class="sep"></span>Brands</nav>
  <div class="abs header-rule"></div>
</header>

<section class="abs hero">
  <div class="abs slider" style="top:18px">
    <div class="abs slide-art" role="img" aria-label="Interior illustration: white sofa, potted plant and framed pictures on a green wall with floral line art"></div>
    <div class="abs slide-bar"><div class="abs dots" style="left:284px;top:15px"><i></i><i></i><i></i><i></i></div></div>
  </div>
  <aside class="abs apps" style="top:18px">
    <div class="abs apps-card">
      <div class="abs apps-title">Application</div>
      <div class="abs app" style="top:54px"><div class="app-thumb" role="img" aria-label="Vehicle wrap application photo"></div><div><h3>Application Name</h3><p>Nam cursus. Morbi ut mi. Nullam enim leo, egestas id, condimentum at, laoreet mattis, massa.</p></div></div>
      <div class="abs app" style="top:144px"><div class="app-thumb" role="img" aria-label="Printed car advert panel photo" style="background:linear-gradient(135deg,#ddd,#8fa0b8)"></div><div><h3>Application Name</h3><p>Nam cursus. Morbi ut mi. Nullam enim leo, egestas id, condimentum at, laoreet mattis, massa.</p></div></div>
      <div class="abs app" style="top:237px;left:27px"><div class="app-thumb" role="img" aria-label="Roll-up display stand photo" style="background:linear-gradient(135deg,#e8eef4,#5d9fd0)"></div><div><h3>Application Name</h3><p>Nam cursus. Morbi ut mi. Nullam enim leo, egestas id, condimentum at, laoreet mattis, massa.</p></div></div>
    </div>
  </aside>
</section>

<main class="abs welcome">
  <h1>Welcome to Our Website Mainpage</h1>
  <p class="lead">Lorem ipsum dolor sit amet, consectetuer adipiscing elit. Nam cursus. Morbi ut mi. Nullam enim leo, egestas id, condimentum at, laoreet mattis, massa. Sed eleifend nonummy diam. Praesent mauris ante, elementum et, bibendum at, posuere sit amet, nibh.</p>
  <p>Duis tincidunt lectus quis dui viverra vestibulum. Suspendisse vulputate aliquam dui. Nulla elementum dui ut augue. Aliquam vehicula mi at mauris. Maecenas placerat, nisl at consequat rhoncus, sem nunc gravida justo, quis eleifend arcu velit quis lacus. Morbi magna magna, tincidunt a, mattis non, imperdiet vitae, tellus. Sed odio est, auctor ac, sollicitudin in, consequat vitae, orci. Fusce id felis. Vivamus sollicitudin metus eget eros.</p>
  <p>Pellentesque habitant morbi tristique senectus et netus et malesuada fames ac turpis egestas. In posuere felis nec tortor. Pellentesque faucibus. Ut accumsan ultricies elit. Maecenas at justo id velit placerat molestie. Donec dictum lectus non odio. Cras a ante vitae enim iaculis aliquam. Mauris nunc quam, venenatis nec, euismod sit amet, egestas placerat, est. Pellentesque habitant morbi tristique senectus et netus et malesuada fames ac turpis egestas</p>
</main>
<div class="abs divider"></div>

<svg class="abs partner-mark" width="64" height="60" viewBox="0 0 64 60" aria-hidden="true"><circle cx="30" cy="29" r="27" fill="none" stroke="#444" stroke-width="1.2"/></svg>
<div class="abs partners"><span>Corvel</span><span>Ansora</span><span>Deltrix</span><span>Hexon</span><span>Lumira</span><span>Maxfield</span><span>Norvia</span><span>Quorra</span></div>

<footer class="abs footer">
  <div class="abs fcol" style="left:67px"><h4>About Company</h4><ul><li>Why We Are</li><li>What We DO</li><li>Our Clients</li><li>Partners</li></ul></div>
  <div class="abs fsep" style="left:205px"></div>
  <div class="abs fcol" style="left:247px"><h4>Advertising</h4><ul><li>Services</li><li>Implementation</li><li>Career</li><li>Jobs</li></ul></div>
  <div class="abs fsep" style="left:376px"></div>
  <div class="abs fcol" style="left:421px"><h4>Displays</h4><ul><li>Services</li><li>Implementation</li><li>Services</li><li>Implementation</li></ul></div>
  <div class="abs fsep" style="left:546px"></div>
  <div class="abs fcol" style="left:597px"><h4>Printing</h4><ul><li>Services</li><li>Implementation</li><li>Services</li><li>Implementation</li></ul></div>
  <div class="abs fsep" style="left:726px"></div>
  <div class="abs fcol contact" style="left:776px"><h4>Contact Information</h4><ul><li><strong>Trumex Advertising &amp; Printing LTD</strong></li><li>Hillcrest 12, Marlow Park 1620&nbsp; NY</li><li>Tele:&nbsp; <span class="tel">+30 2100457302</span></li><li>Email:&nbsp; <u>info@trumexsign.gr</u></li></ul></div>
</footer>
<div class="abs bottom">
  <div class="abs copy">© 2012 Company Name.&nbsp; All right reserved.&nbsp; Term of Use</div>
  <div class="abs social"><i></i><i></i><i></i></div>
</div>
</body>
</html>
```